Adapt logo for box truck wrap for my restoration company

I need a wrap for our company Brightway Restoration. We specialize in water damage restoration. I’ve attached our logo, business card, and page header. Things I would like to include are- 24 hour emergency service, our phone number (555)014-7392 and that we do water, fire and mold work. It’s a 2004 Kardella Vonter which I’ve attached pictures of. I will get the cab wrapped as well.

Industry/Entity Type

Construction- specifically Restoration

Font styles to use
Sans Serif

Colors

Designer to choose colors to be used in the design.

Requirements
Must have
• Water• Fire• Mold, phone number (555)014-7392
Nice to have
• Clean, professional look with the logo

```html
<!DOCTYPE html>
<html lang="en">
<head>
<meta charset="utf-8">
<title>Brightway Restoration – Box Truck Side Wrap</title>
<link rel="stylesheet" href="https://fonts.googleapis.com/css2?family=Bebas+Neue&display=swap">
<style>
  :root {
    --panel-bg: #dfeaf5;
    --brand-blue: #1683d8;
    --brand-grey: #6d7073;
    --ink: #0d0d0d;
    --white: #ffffff;
    --photo-dark: #4a3a2c;
    --photo-light: #a08a70;
  }
  html, body {
    margin: 0;
    padding: 0;
    width: 1200px;
    height: 656px;
    overflow: hidden;
    background: #ffffff;
  }
  .wrap-panel {
    display: block;
    width: 1200px;
    height: 656px;
  }
  .display-type { font-family: "Bebas Neue", sans-serif; }
  .web-address { font-style: italic; fill: var(--ink); }
  .headline-grey { fill: var(--brand-grey); }
  .headline-blue { fill: var(--brand-blue); }
  .tagline { fill: var(--brand-blue); }
  .services { fill: var(--ink); }
  .phone { fill: var(--white); }
  .badge-text { fill: var(--white); }
  .logo-name { fill: var(--brand-grey); }
</style>
</head>
<body>
<svg class="wrap-panel" viewBox="0 0 1200 656" xmlns="http://www.w3.org/2000/svg">
  <defs>
    <linearGradient id="photoTone" x1="0" y1="0" x2="1" y2="1">
      <stop offset="0" stop-color="var(--photo-dark)"/>
      <stop offset="0.55" stop-color="var(--photo-light)"/>
      <stop offset="1" stop-color="var(--photo-dark)"/>
    </linearGradient>
    <linearGradient id="curlTone" x1="0" y1="0" x2="1" y2="0.3">
      <stop offset="0" stop-color="#c9ccd0"/>
      <stop offset="0.5" stop-color="#ffffff"/>
      <stop offset="1" stop-color="#e6e8ea"/>
    </linearGradient>
  </defs>

  <!-- panel background -->
  <rect class="panel-base" x="0" y="0" width="1200" height="656" fill="var(--panel-bg)"/>

  <!-- top band and stripes -->
  <polygon class="top-band" points="0,0 1200,0 1200,22 400,22 360,54 0,54" fill="var(--brand-blue)"/>
  <g class="top-stripes-light" fill="var(--panel-bg)">
    <polygon points="610,22 626,0 636,0 620,22"/>
    <polygon points="650,22 666,0 676,0 660,22"/>
    <polygon points="690,22 706,0 716,0 700,22"/>
    <polygon points="730,22 746,0 756,0 740,22"/>
    <polygon points="770,22 786,0 796,0 780,22"/>
    <polygon points="810,22 826,0 836,0 820,22"/>
    <polygon points="850,22 866,0 876,0 860,22"/>
    <polygon points="890,22 906,0 916,0 900,22"/>
    <polygon points="930,22 946,0 956,0 940,22"/>
    <polygon points="970,22 986,0 996,0 980,22"/>
    <polygon points="1010,22 1026,0 1036,0 1020,22"/>
    <polygon points="1050,22 1066,0 1200,0 1200,22"/>
  </g>

  <!-- web address -->
  <text class="display-type web-address" x="604" y="92" font-size="36" text-anchor="middle" textLength="470" lengthAdjust="spacingAndGlyphs">BRIGHTWAYRESTORATIONPRO.COM</text>

  <!-- logo area: plain circle with name -->
  <g class="logo-mark">
    <circle cx="159" cy="262" r="128" fill="none" stroke="var(--brand-blue)" stroke-width="26"/>
    <text class="display-type logo-name" x="159" y="282" font-size="60" text-anchor="middle" textLength="190" lengthAdjust="spacingAndGlyphs">BRIGHTWAY</text>
  </g>

  <!-- headline -->
  <text class="display-type headline" x="304" y="226" font-size="84" textLength="596" lengthAdjust="spacingAndGlyphs"><tspan class="headline-grey">BRIGHTWAY </tspan><tspan class="headline-blue">RESTORATION</tspan></text>

  <!-- tagline -->
  <text class="display-type tagline" x="308" y="298" font-size="40" textLength="560" lengthAdjust="spacingAndGlyphs">WE SPECIALIZE IN WATER DAMAGE  RESTORATION</text>

  <!-- services -->
  <text class="display-type services" x="306" y="390" font-size="86" textLength="536" lengthAdjust="spacingAndGlyphs">WATER • FIRE • MOLD</text>

  <!-- grey divider -->
  <rect class="divider" x="0" y="449" width="880" height="20" fill="var(--brand-grey)"/>

  <!-- phone band -->
  <polygon class="phone-band" points="0,486 860,486 790,640 0,640" fill="var(--brand-blue)"/>
  <polygon class="phone-band-accent" points="0,584 42,584 72,640 0,640" fill="var(--ink)"/>
  <rect class="bottom-stripes" x="238" y="640" width="460" height="14" fill="var(--ink)"/>
  <g class="bottom-stripes-gap" fill="var(--panel-bg)">
    <polygon points="250,654 258,640 264,640 256,654"/>
    <polygon points="272,654 280,640 286,640 278,654"/>
    <polygon points="294,654 302,640 308,640 300,654"/>
    <polygon points="316,654 324,640 330,640 322,654"/>
    <polygon points="338,654 346,640 352,640 344,654"/>
    <polygon points="360,654 368,640 374,640 366,654"/>
    <polygon points="382,654 390,640 396,640 388,654"/>
    <polygon points="404,654 412,640 418,640 410,654"/>
    <polygon points="426,654 434,640 440,640 432,654"/>
    <polygon points="448,654 456,640 462,640 454,654"/>
    <polygon points="470,654 478,640 484,640 476,654"/>
    <polygon points="492,654 500,640 506,640 498,654"/>
    <polygon points="514,654 522,640 528,640 520,654"/>
    <polygon points="536,654 544,640 550,640 542,654"/>
    <polygon points="558,654 566,640 572,640 564,654"/>
    <polygon points="580,654 588,640 594,640 586,654"/>
    <polygon points="602,654 610,640 616,640 608,654"/>
    <polygon points="624,654 632,640 638,640 630,654"/>
    <polygon points="646,654 654,640 660,640 652,654"/>
    <polygon points="668,654 676,640 682,640 674,654"/>
  </g>

  <!-- emergency badge -->
  <g class="emergency-badge">
    <path d="M100,575 A52,52 0 1 1 204,575" fill="none" stroke="var(--ink)" stroke-width="7"/>
    <text class="display-type badge-text" x="152" y="573" font-size="44" text-anchor="middle">24/H</text>
    <text class="display-type badge-text" x="152" y="600" font-size="22" text-anchor="middle" font-style="italic">EMERGENCY SERVICE</text>
  </g>

  <!-- phone -->
  <text class="display-type phone" x="280" y="605" font-size="104" textLength="480" lengthAdjust="spacingAndGlyphs">(555)014-7392</text>

  <!-- restoration work photo -->
  <path class="work-photo" role="img" aria-label="Photo of a technician extracting muddy water from a flooded floor" d="M1160,0 L1200,0 L1200,656 L770,656 L1160,160 Z" fill="url(#photoTone)"/>

  <!-- page curl -->
  <path class="page-curl" d="M1000,92 C1066,66 1132,100 1160,160 L770,656 C830,520 930,290 1000,92 Z" fill="url(#curlTone)"/>

  <!-- service photo circles -->
  <g class="service-photos" stroke="var(--brand-blue)" stroke-width="3">
    <circle cx="934" cy="551" r="40" fill="#b89a78" role="img" aria-label="Photo of a wet floor being cleaned"/>
    <circle cx="1027" cy="551" r="40" fill="#cfcbc3" role="img" aria-label="Close-up photo of mold growth"/>
    <circle cx="1118" cy="551" r="40" fill="#8a7a68" role="img" aria-label="Photo of a worker in protective suit treating a surface"/>
  </g>
</svg>
</body>
</html>
```